Consultant Firm Marketing Flyer

I want to use this flyer to market health care consultant services. I would like a front and back glossy, professional, yet bold and eye catching design. I would like it to convey knowledge, expertise, partnership and strength. The colors should blue and white but I am very open to the designer being creative. You can visit my website to see colors and images I want to use at brightharborcare.net
I would like the home page image on my website to be incorporated into the flyer but I am also open to other images that work with the design. The designer can be creative.

I want to highlight 4 service area’s of focus to my clients:
1. Revenue Cycle Optimization (making my clients money)
2. Practice Management Optimization (improving clinical operations)
3. Health Compliance (following the law)
4. Health Care Technology: (Telemedicine and AI)
Please be creative. Go where ever your creativity leads.

```html
<!DOCTYPE html>
<html lang="en">
<head>
<meta charset="utf-8">
<title>Bright Harbor Care – Flyer</title>
<link href="https://fonts.googleapis.com/css2?family=Exo+2:wght@600;700&family=Montserrat:wght@400;600;700&family=Questrial&display=swap" rel="stylesheet">
<style>
:root{
  --bg:#3d3d3d;
  --navy:#0d4fa0;
  --royal:#0b5cb0;
  --sky:#2ea3dc;
  --paper:#ffffff;
  --ink:#1c1c1c;
  --muted:#333;
  --line:#555;
}
*{margin:0;padding:0;box-sizing:border-box}
html,body{width:1200px;height:1200px;overflow:hidden;background:var(--bg)}
.canvas{position:relative;width:1200px;height:1200px}
.page{position:absolute;background:var(--paper);overflow:hidden}
.front{left:93px;top:281px;width:473px;height:662px}
.back{left:624px;top:281px;width:475px;height:667px}
.layer{position:absolute;left:0;top:0}
.abs{position:absolute}

/* front */
.brand{left:0;width:100%;top:398px;text-align:center;font-family:"Montserrat",sans-serif}
.brand-mark{font-weight:700;font-size:30px;color:var(--royal);letter-spacing:1px;line-height:32px}
.brand-sub{font-family:"Questrial",sans-serif;font-size:8.5px;color:var(--ink);letter-spacing:.6px;margin-top:2px}
.welcome{left:0;width:100%;top:451px;text-align:center;font-family:"Montserrat",sans-serif;font-weight:700;font-size:19.5px;color:var(--royal);letter-spacing:.3px}
.tagline{left:0;width:100%;top:478px;text-align:center;font-family:"Questrial",sans-serif;font-size:21px;color:var(--ink)}
.intro{left:18px;top:516px;width:442px;font-family:"Questrial",sans-serif;font-size:9.3px;line-height:11.2px;color:var(--ink)}
.intro p+p{margin-top:6px}
.front-url{left:0;width:100%;top:637px;text-align:center;font-family:"Montserrat",sans-serif;font-size:10px;letter-spacing:.8px;color:var(--paper)}

/* back */
.whatwedo{left:289px;top:26px;font-family:"Exo 2",sans-serif;font-weight:600;font-size:23px;color:var(--paper)}
.point{left:272px;width:196px;color:var(--paper)}
.point svg{position:absolute;left:0;top:1px}
.point h3{margin-left:17px;font-family:"Montserrat",sans-serif;font-weight:700;font-size:8.6px;line-height:10px;letter-spacing:.2px}
.point p{margin-left:17px;margin-top:3px;font-family:"Questrial",sans-serif;font-size:6.4px;line-height:8.4px;opacity:.95}
.services-title{left:183px;top:279px;font-family:"Exo 2",sans-serif;font-weight:700;font-size:23px;color:var(--ink)}
.service-icon{left:20px;width:43px;height:43px;border-radius:50%;background:var(--royal);box-shadow:0 0 0 2px #fff inset,0 0 0 3px var(--royal) inset}
.service-icon svg{display:block}
.service-name{left:69px;font-family:"Exo 2",sans-serif;font-weight:700;font-size:11px;line-height:13px;color:var(--ink);letter-spacing:.3px}
.service-dash{left:172px;width:9px;height:1.5px;background:var(--ink)}
.service-box{left:182px;width:284px;border:1px solid var(--line);padding:4px 5px;font-family:"Questrial",sans-serif;font-size:7.7px;line-height:9.2px;color:var(--muted);text-align:justify}
.back-url{left:22px;top:630px;font-family:"Montserrat",sans-serif;font-size:10.5px;letter-spacing:1px;color:var(--paper)}
.contact{right:38px;text-align:right;font-family:"Montserrat",sans-serif;font-size:7.3px;letter-spacing:.6px;color:var(--paper);line-height:9px}
.contact-icon{left:444px}
</style>
</head>
<body>
<div class="canvas">

  <!-- FRONT PAGE -->
  <section class="page front">
    <svg class="layer" width="473" height="662" viewBox="0 0 473 662">
      <defs>
        <linearGradient id="frontPhoto" x1="0" y1="0" x2="1" y2="1">
          <stop offset="0" stop-color="#e9eef2"/>
          <stop offset=".55" stop-color="#b9c2cc"/>
          <stop offset="1" stop-color="#7d6470"/>
        </linearGradient>
      </defs>
      <polygon points="0,0 473,0 473,313 0,380" fill="url(#frontPhoto)" role="img" aria-label="Photo of four healthcare professionals meeting around a table in a bright office"/>
      <polygon points="0,380 473,313 473,359 0,396" fill="var(--navy)"/>
      <polygon points="0,614 473,625 473,662 0,662" fill="var(--sky)"/>
      <polygon points="0,640 260,632 473,612 473,662 0,662" fill="var(--navy)"/>
    </svg>
    <div class="abs brand">
      <div class="brand-mark">BHC</div>
      <div class="brand-sub">BRIGHT HARBOR CARE LLC</div>
    </div>
    <h1 class="abs welcome">WELCOME TO BRIGHT HARBOR CARE</h1>
    <h2 class="abs tagline">Advancing Healthcare Operations</h2>
    <div class="abs intro">
      <p>Bright Harbor Care (BHC) is a healthcare consulting firm skilled at helping physician practices advance their strategic vision in an ever-evolving healthcare system. Bright Harbor Care specializes in revenue cycle optimization, practice management improvement and developing new physician practices. Our technical skills allow us to dig deep into your revenue cycle while our strategic approach ensures we’re keeping our eyes on the entire financial picture.</p>
      <p>The varied expertise of our team encompass full service revenue cycle management, practice management, regulatory compliance, human resource management, and full spectrum health care consulting services.</p>
    </div>
    <div class="abs front-url">www.brightharborcare.net</div>
  </section>

  <!-- BACK PAGE -->
  <section class="page back">
    <svg class="layer" width="475" height="667" viewBox="0 0 475 667">
      <defs>
        <linearGradient id="backPhoto" x1="0" y1="0" x2="1" y2="0">
          <stop offset="0" stop-color="#cfd6dc"/>
          <stop offset=".35" stop-color="#a9b6c0"/>
          <stop offset=".55" stop-color="#6fb4de"/>
          <stop offset=".7" stop-color="#3aa6df"/>
          <stop offset="1" stop-color="#2ea3dc"/>
        </linearGradient>
      </defs>
      <polygon points="0,0 475,0 475,0 0,40" fill="var(--navy)"/>
      <polygon points="0,0 360,0 0,32" fill="var(--navy)"/>
      <polygon points="0,40 475,8 475,262 0,286" fill="url(#backPhoto)" role="img" aria-label="Photo of two colleagues reviewing reports on a laptop in an office"/>
      <polygon points="0,582 475,596 475,667 0,667" fill="var(--sky)"/>
      <polygon points="0,610 200,604 475,582 475,667 0,667" fill="var(--navy)"/>
    </svg>

    <h2 class="abs whatwedo">What we do</h2>

    <div class="abs point" style="top:62px">
      <svg width="12" height="11" viewBox="0 0 12 11"><rect x=".5" y="2" width="8" height="8" fill="none" stroke="#fff"/><path d="M2.5 5.5l2.5 2.5L11 1" fill="none" stroke="#fff" stroke-width="1.8"/></svg>
      <h3>$999,000 HIPAA SETTLEMENT</h3>
      <p>Unauthorized Disclosure of Patients’ Protected Health Information During “City Med” Filming Results in Multiple HIPAA Settlements Totaling $999,000</p>
    </div>
    <div class="abs point" style="top:125px">
      <svg width="12" height="11" viewBox="0 0 12 11"><rect x=".5" y="2" width="8" height="8" fill="none" stroke="#fff"/><path d="M2.5 5.5l2.5 2.5L11 1" fill="none" stroke="#fff" stroke-width="1.8"/></svg>
      <h3>COMMON PROBLEMS IN MEDICAL CODING</h3>
      <p>NOT coding the highest level.The coder’s job is to code to the highest level of specificity.This means abstracting the most information out of the medical reports from the provider and taking accurate notes.</p>
    </div>
    <div class="abs point" style="top:216px">
      <svg width="12" height="11" viewBox="0 0 12 11"><rect x=".5" y="2" width="8" height="8" fill="none" stroke="#fff"/><path d="M2.5 5.5l2.5 2.5L11 1" fill="none" stroke="#fff" stroke-width="1.8"/></svg>
      <h3>REVENUE CYCLE CHALLENGES</h3>
      <p>Inattention to a billing process can hurt hospitals to the tune of tens of millions of dollars, and may also shock patients with huge debts that they cannot pay.</p>
    </div>

    <h2 class="abs services-title">Our Services</h2>

    <!-- service 1 -->
    <div class="abs service-icon" style="top:308px">
      <svg width="43" height="43" viewBox="0 0 43 43"><path d="M13 22a8.5 8.5 0 0 1 14-6.5" fill="none" stroke="#fff" stroke-width="2.6"/><path d="M30 21a8.5 8.5 0 0 1-14 6.5" fill="none" stroke="#fff" stroke-width="2.6"/><path d="M25 12l4 4-5 1.5z" fill="#fff"/><path d="M18 31l-4-4 5-1.5z" fill="#fff"/></svg>
    </div>
    <div class="abs service-name" style="top:316px">REVENUE CYCLE<br>MANAGEMENT</div>
    <div class="abs service-dash" style="top:334px"></div>
    <div class="abs service-box" style="top:313px;height:48px">In today’s increasingly complex health care environment it’s important now more than ever that medical practices closely manage their revenue cycle. Bright Harbor Care (BHC) understands the reimbursement landscape</div>

    <!-- service 2 -->
    <div class="abs service-icon" style="top:388px">
      <svg width="43" height="43" viewBox="0 0 43 43"><rect x="13" y="11" width="16" height="21" rx="2" fill="none" stroke="#fff" stroke-width="2"/><path d="M21 15l5 2v4c0 3-2.2 5-5 6-2.8-1-5-3-5-6v-4z" fill="#fff"/><path d="M18.5 20.5l2 2 3.5-4" fill="none" stroke="var(--royal)" stroke-width="1.5"/></svg>
    </div>
    <div class="abs service-name" style="top:396px">REGULATORY<br>COMPLIANCE</div>
    <div class="abs service-dash" style="top:404px"></div>
    <div class="abs service-box" style="top:378px;height:53px">In a heavily regulated healthcare environment medical practices need to be acutely aware of regulations as they present huge liabilities. It is extremely important to ensure compliance with regulations. BHC offers a host of comprehensive compliance services.</div>

    <!-- service 3 -->
    <div class="abs service-icon" style="top:457px">
      <svg width="43" height="43" viewBox="0 0 43 43"><circle cx="21.5" cy="21.5" r="10" fill="none" stroke="#fff" stroke-width="3" stroke-dasharray="4 3"/><circle cx="21.5" cy="19" r="3.2" fill="#fff"/><path d="M15.5 28c1-4 3.5-5 6-5s5 1 6 5z" fill="#fff"/></svg>
    </div>
    <div class="abs service-name" style="top:469px">HUMAN RESOURCE<br>MANAGEMENT</div>
    <div class="abs service-dash" style="top:477px"></div>
    <div class="abs service-box" style="top:450px;height:53px">Do you need Human Resources Management but don’t want the expense of a full service Human Resources Department? Not having a full service Human Resources Department can increase liability and be costly to your medical practice.</div>

    <!-- service 4 -->
    <div class="abs service-icon" style="top:527px">
      <svg width="43" height="43" viewBox="0 0 43 43"><circle cx="21.5" cy="16" r="4.5" fill="none" stroke="#fff" stroke-width="2.4" stroke-dasharray="3 1.6"/><path d="M11 22c2 4 5 7 10 9M32 22c-2 4-5 7-10 9" fill="none" stroke="#fff" stroke-width="2.6" stroke-linecap="round"/></svg>
    </div>
    <div class="abs service-name" style="top:542px">PRACTICE<br>MANAGEMENT</div>
    <div class="abs service-dash" style="top:547px"></div>
    <div class="abs service-box" style="top:521px;height:53px">Practice Management is challenging and it requires the right balance of skill, knowledge, experience and management expertise. BHC Offers assessment and optimization in Patient Access &amp; Scheduling, Patient Experience, Staff Experience</div>

    <!-- footer -->
    <div class="abs back-url">BRIGHTHARBORCARE.NET</div>
    <div class="abs contact" style="top:602px">118 LINDEN ST SUITE 4B<br>118 Linden St, Riverton, NJ 08077, USA</div>
    <div class="abs contact" style="top:632px">(555) 214-0370</div>
    <div class="abs contact" style="top:652px">info@brightharborcare.net</div>
    <svg class="abs contact-icon" style="top:600px" width="14" height="16" viewBox="0 0 14 16"><path d="M7 1a5.5 5.5 0 0 1 5.5 5.5C12.5 10.5 7 15 7 15S1.5 10.5 1.5 6.5A5.5 5.5 0 0 1 7 1z" fill="#fff"/><circle cx="7" cy="6.5" r="2" fill="var(--navy)"/></svg>
    <svg class="abs contact-icon" style="top:627px" width="16" height="16" viewBox="0 0 16 16"><circle cx="8" cy="8" r="7" fill="none" stroke="#fff" stroke-width="1.3"/><path d="M5.5 4.5l1.5 2-1 1c.6 1.2 1.3 1.9 2.5 2.5l1-1 2 1.5-1 1.5c-3 0-6-3-6-6z" fill="#fff"/></svg>
    <svg class="abs contact-icon" style="top:651px" width="16" height="12" viewBox="0 0 16 12"><rect x=".5" y=".5" width="15" height="11" fill="#fff"/><path d="M.5 .5L8 7l7.5-6.5M.5 11.5L6 6M15.5 11.5L10 6" fill="none" stroke="var(--navy)" stroke-width="1.2"/></svg>
  </section>

</div>
</body>
</html>
```